2019/20 Season Calendar (This is to be at the top of the calendar as title)

An advertising calendar for our agricultural business to explain our key business attributes and give clients a nice looking calendar to refer to .

Please refer to doc/pdf attachments for text details and ideas. (Our current logo needs to be incorporated - this logo can be altered if need be)

open to professional agriculture aesthetics keeping in line with the companies Green colour scheme (logo)

The calendar is to start at October 2019 - September 2020

97mm x 122mm

Target Market(s)

Agricultural sector (professional)

Industry/Entity Type

Agriculture

Font styles to use
Sans Serif

Colors
abd036
3276b5

Requirements
Must have
• Calender with dates starting october 1st 2019 finishing end of september 2020.
• Must include all public holidays etc for Australia during this time.
• contact details including website :www.brevardholdings.com.au
Nice to have
• In the calendar the months of
• October/ nov /december (be coloured yellow)
• April/May/June (be coloured brown)
• July /aug/september (be coloured green)
• Jan/feb/march (be coloured white)
• Then in the corner of the calendar a key (like a map) to refer to the colours
• [a small square with the colour yellow] (next to the square the following text) Harvesting
• [a small square with the colour brown] (next to the square the following text) Sowing
• [a small square with the colour green] (next to the square the following text) Growing
• [a small square with the colour white] (next to the square the following text) Liming + Fertilising

```html
<!DOCTYPE html>
<html lang="en">
<head>
<meta charset="utf-8">
<title>2019/20 Season Calendar</title>
<link rel="stylesheet" href="https://fonts.googleapis.com/css2?family=Montserrat:ital,wght@0,400;0,500;0,700;0,800;1,400&family=Saira+Condensed:wght@200;300&family=Oswald:wght@500;600&display=swap">
<style>
:root{
  --bg:#e9d6da;
  --paper:#f7f7f6;
  --ink:#2b2b2b;
  --harvest:#c9d400;
  --liming:#a4c83a;
  --sowing:#6e4c1e;
  --growing:#2a9d47;
  --brand-green:#abd036;
  --brand-blue:#3276b5;
  --sky-top:#3b7fc4;
  --sky-low:#9cc4e6;
  --ground:#8b7d6a;
}
*{margin:0;padding:0;box-sizing:border-box}
html,body{width:1200px;height:900px;overflow:hidden;background:var(--bg)}
body{font-family:"Montserrat",sans-serif;color:var(--ink);position:relative}
.calendar{position:absolute;left:300px;top:20px;width:600px;height:860px;background:var(--paper);overflow:hidden;box-shadow:0 10px 30px rgba(80,40,50,.25)}
.hero{position:absolute;left:0;top:0;width:600px;height:315px;background:linear-gradient(180deg,var(--sky-top) 0%,var(--sky-low) 45%,#c9ccd0 62%,var(--ground) 100%)}
.hero-edge{position:absolute;left:0;top:250px;width:600px;height:80px}
.title{position:absolute;right:13px;top:12px;text-align:right;color:#fff}
.title-year{font-family:"Saira Condensed",sans-serif;font-weight:200;font-size:70px;line-height:64px;letter-spacing:-1px}
.title-sub{font-weight:800;font-size:19.5px;letter-spacing:.2px;margin-top:8px;text-shadow:0 1px 3px rgba(0,0,0,.3)}
.month{position:absolute;width:135px}
.month-head{position:relative;height:15px;border-bottom:2px solid var(--m)}
.month-tag{position:absolute;left:0;bottom:0;height:11px;padding:0 12px 0 5px;background:var(--m);color:#fff;font-size:6.6px;font-weight:500;line-height:11px;clip-path:polygon(0 0,86% 0,100% 100%,0 100%)}
.month-year{position:absolute;right:0;bottom:0;font-family:"Saira Condensed",sans-serif;font-weight:300;font-size:15px;line-height:15px;color:var(--m)}
.weekdays,.days{display:grid;grid-template-columns:repeat(7,1fr);text-align:center}
.weekdays{font-size:6.4px;font-weight:500;margin-top:5px;height:12px}
.weekdays span:first-child{color:var(--m)}
.days{font-size:6.6px;font-weight:500;grid-auto-rows:14.2px;line-height:14.2px;margin-top:1px}
.days span:nth-child(7n+1),.days .hol{color:var(--m)}
.season-harvest{--m:var(--harvest)}
.season-liming{--m:var(--liming)}
.season-sowing{--m:var(--sowing)}
.season-growing{--m:var(--growing)}
.key{position:absolute;right:0;width:26px;display:flex;align-items:center;justify-content:center;border-right:6px solid var(--m)}
.key-label{writing-mode:vertical-rl;transform:rotate(180deg);font-family:"Oswald",sans-serif;font-weight:600;font-size:17px;color:var(--m);letter-spacing:.2px}
.key-label.small{font-size:10px;font-weight:500}
.footer{position:absolute;left:0;top:800px;width:600px;height:60px}
.brand{position:absolute;left:60px;top:9px;width:88px}
.brand-name{display:flex;align-items:center;gap:4px;font-weight:800;font-size:10px;line-height:10.5px;color:var(--growing);border-bottom:1.5px solid var(--growing);padding-bottom:3px}
.brand-mark{width:12px;height:12px;background:var(--growing);flex:none}
.brand-tag{font-size:3.6px;font-weight:700;color:var(--growing);margin-top:2px;white-space:nowrap}
.services{position:absolute;left:158px;top:6px;list-style:none;font-size:5.6px;font-style:italic;line-height:9px;color:#444}
.contact{position:absolute;left:317px;top:9px;border-left:1px solid var(--growing);padding-left:4px;font-size:6.2px;line-height:10px}
.contact-icons{position:absolute;left:-11px;top:0;display:flex;flex-direction:column}
.contact-icons svg{width:6px;height:6px;margin:2px 0}
.address{position:absolute;left:467px;top:9px;border-left:1px solid var(--growing);padding-left:4px;font-size:6.2px;line-height:10px}
.address-icon{position:absolute;left:-10px;top:2px;width:6px;height:6px}
.base{position:absolute;left:0;bottom:0;width:600px;height:18px}
</style>
</head>
<body>
<main class="calendar">
  <div class="hero" role="img" aria-label="Photo of a grain storage shed with silos and a green prime mover truck under a clear blue sky"></div>
  <svg class="hero-edge" viewBox="0 0 600 80" preserveAspectRatio="none" aria-hidden="true">
    <polygon points="0,80 0,64 600,22 600,80" fill="var(--brand-green)"/>
    <polygon points="380,46 600,14 600,45" fill="var(--brand-blue)"/>
    <polygon points="0,80 0,66 600,44 600,80" fill="var(--paper)"/>
  </svg>
  <header class="title">
    <div class="title-year">2019/20</div>
    <div class="title-sub">SEASON CALENDAR</div>
  </header>

  <!-- Row 1 -->
  <section class="month season-harvest" style="left:74px;top:327px">
    <div class="month-head"><span class="month-tag">OCTOBER</span><span class="month-year">2019</span></div>
    <div class="weekdays"><span>SUN</span><span>MON</span><span>TUE</span><span>WED</span><span>THU</span><span>FRI</span><span>SAT</span></div>
    <div class="days"><span></span><span></span><span>1</span><span>2</span><span>3</span><span>4</span><span>5</span><span>6</span><span>7</span><span>8</span><span>9</span><span>10</span><span>11</span><span>12</span><span>13</span><span>14</span><span>15</span><span>16</span><span>17</span><span>18</span><span>19</span><span>20</span><span>21</span><span>22</span><span>23</span><span>24</span><span>25</span><span>26</span><span>27</span><span>28</span><span>29</span><span>30</span><span>31</span></div>
  </section>
  <section class="month season-harvest" style="left:231px;top:327px">
    <div class="month-head"><span class="month-tag">NOVEMBER</span><span class="month-year">2019</span></div>
    <div class="weekdays"><span>SUN</span><span>MON</span><span>TUE</span><span>WED</span><span>THU</span><span>FRI</span><span>SAT</span></div>
    <div class="days"><span></span><span></span><span></span><span></span><span></span><span>1</span><span>2</span><span>3</span><span>4</span><span>5</span><span>6</span><span>7</span><span>8</span><span>9</span><span>10</span><span>11</span><span>12</span><span>13</span><span>14</span><span>15</span><span>16</span><span>17</span><span>18</span><span>19</span><span>20</span><span>21</span><span>22</span><span>23</span><span>24</span><span>25</span><span>26</span><span>27</span><span>28</span><span>29</span><span>30</span></div>
  </section>
  <section class="month season-harvest" style="left:387px;top:327px">
    <div class="month-head"><span class="month-tag">DECEMBER</span><span class="month-year">2019</span></div>
    <div class="weekdays"><span>SUN</span><span>MON</span><span>TUE</span><span>WED</span><span>THU</span><span>FRI</span><span>SAT</span></div>
    <div class="days"><span>1</span><span>2</span><span>3</span><span>4</span><span>5</span><span>6</span><span>7</span><span>8</span><span>9</span><span>10</span><span>11</span><span>12</span><span>13</span><span>14</span><span>15</span><span>16</span><span>17</span><span>18</span><span>19</span><span>20</span><span>21</span><span>22</span><span>23</span><span>24</span><span class="hol">25</span><span class="hol">26</span><span>27</span><span>28</span><span>29</span><span>30</span><span>31</span></div>
  </section>

  <!-- Row 2 -->
  <section class="month season-liming" style="left:74px;top:444px">
    <div class="month-head"><span class="month-tag">JANUARY</span><span class="month-year">2020</span></div>
    <div class="weekdays"><span>SUN</span><span>MON</span><span>TUE</span><span>WED</span><span>THU</span><span>FRI</span><span>SAT</span></div>
    <div class="days"><span></span><span></span><span></span><span class="hol">1</span><span>2</span><span>3</span><span>4</span><span>5</span><span>6</span><span>7</span><span>8</span><span>9</span><span>10</span><span>11</span><span>12</span><span>13</span><span>14</span><span>15</span><span>16</span><span>17</span><span>18</span><span>19</span><span>20</span><span>21</span><span>22</span><span>23</span><span>24</span><span>25</span><span>26</span><span class="hol">27</span><span>28</span><span>29</span><span>30</span><span>31</span></div>
  </section>
  <section class="month season-liming" style="left:231px;top:444px">
    <div class="month-head"><span class="month-tag">FEBRUARY</span><span class="month-year">2020</span></div>
    <div class="weekdays"><span>SUN</span><span>MON</span><span>TUE</span><span>WED</span><span>THU</span><span>FRI</span><span>SAT</span></div>
    <div class="days"><span></span><span></span><span></span><span></span><span></span><span></span><span>1</span><span>2</span><span>3</span><span>4</span><span>5</span><span>6</span><span>7</span><span>8</span><span>9</span><span>10</span><span>11</span><span>12</span><span>13</span><span>14</span><span>15</span><span>16</span><span>17</span><span>18</span><span>19</span><span>20</span><span>21</span><span>22</span><span>23</span><span>24</span><span>25</span><span>26</span><span>27</span><span>28</span><span>29</span></div>
  </section>
  <section class="month season-liming" style="left:387px;top:444px">
    <div class="month-head"><span class="month-tag">MARCH</span><span class="month-year">2020</span></div>
    <div class="weekdays"><span>SUN</span><span>MON</span><span>TUE</span><span>WED</span><span>THU</span><span>FRI</span><span>SAT</span></div>
    <div class="days"><span>1</span><span>2</span><span>3</span><span>4</span><span>5</span><span>6</span><span>7</span><span>8</span><span>9</span><span>10</span><span>11</span><span>12</span><span>13</span><span>14</span><span>15</span><span>16</span><span>17</span><span>18</span><span>19</span><span>20</span><span>21</span><span>22</span><span>23</span><span>24</span><span>25</span><span>26</span><span>27</span><span>28</span><span>29</span><span>30</span><span>31</span></div>
  </section>

  <!-- Row 3 -->
  <section class="month season-sowing" style="left:74px;top:563px">
    <div class="month-head"><span class="month-tag">APRIL</span><span class="month-year">2020</span></div>
    <div class="weekdays"><span>SUN</span><span>MON</span><span>TUE</span><span>WED</span><span>THU</span><span>FRI</span><span>SAT</span></div>
    <div class="days"><span></span><span></span><span></span><span>1</span><span>2</span><span>3</span><span>4</span><span>5</span><span>6</span><span>7</span><span>8</span><span>9</span><span class="hol">10</span><span class="hol">11</span><span>12</span><span class="hol">13</span><span>14</span><span>15</span><span>16</span><span>17</span><span>18</span><span>19</span><span>20</span><span>21</span><span>22</span><span>23</span><span>24</span><span class="hol">25</span><span>26</span><span>27</span><span>28</span><span>29</span><span>30</span></div>
  </section>
  <section class="month season-sowing" style="left:231px;top:563px">
    <div class="month-head"><span class="month-tag">MAY</span><span class="month-year">2020</span></div>
    <div class="weekdays"><span>SUN</span><span>MON</span><span>TUE</span><span>WED</span><span>THU</span><span>FRI</span><span>SAT</span></div>
    <div class="days"><span></span><span></span><span></span><span></span><span></span><span>1</span><span>2</span><span>3</span><span>4</span><span>5</span><span>6</span><span>7</span><span>8</span><span>9</span><span>10</span><span>11</span><span>12</span><span>13</span><span>14</span><span>15</span><span>16</span><span>17</span><span>18</span><span>19</span><span>20</span><span>21</span><span>22</span><span>23</span><span>24</span><span>25</span><span>26</span><span>27</span><span>28</span><span>29</span><span>30</span><span>31</span></div>
  </section>
  <section class="month season-sowing" style="left:387px;top:563px">
    <div class="month-head"><span class="month-tag">JUNE</span><span class="month-year">2020</span></div>
    <div class="weekdays"><span>SUN</span><span>MON</span><span>TUE</span><span>WED</span><span>THU</span><span>FRI</span><span>SAT</span></div>
    <div class="days"><span></span><span>1</span><span>2</span><span>3</span><span>4</span><span>5</span><span>6</span><span>7</span><span class="hol">8</span><span>9</span><span>10</span><span>11</span><span>12</span><span>13</span><span>14</span><span>15</span><span>16</span><span>17</span><span>18</span><span>19</span><span>20</span><span>21</span><span>22</span><span>23</span><span>24</span><span>25</span><span>26</span><span>27</span><span>28</span><span>29</span><span>30</span></div>
  </section>

  <!-- Row 4 -->
  <section class="month season-growing" style="left:74px;top:682px">
    <div class="month-head"><span class="month-tag">JULY</span><span class="month-year">2020</span></div>
    <div class="weekdays"><span>SUN</span><span>MON</span><span>TUE</span><span>WED</span><span>THU</span><span>FRI</span><span>SAT</span></div>
    <div class="days"><span></span><span></span><span></span><span>1</span><span>2</span><span>3</span><span>4</span><span>5</span><span>6</span><span>7</span><span>8</span><span>9</span><span>10</span><span>11</span><span>12</span><span>13</span><span>14</span><span>15</span><span>16</span><span>17</span><span>18</span><span>19</span><span>20</span><span>21</span><span>22</span><span>23</span><span>24</span><span>25</span><span>26</span><span>27</span><span>28</span><span>29</span><span>30</span><span>31</span></div>
  </section>
  <section class="month season-growing" style="left:231px;top:682px">
    <div class="month-head"><span class="month-tag">AUGUST</span><span class="month-year">2020</span></div>
    <div class="weekdays"><span>SUN</span><span>MON</span><span>TUE</span><span>WED</span><span>THU</span><span>FRI</span><span>SAT</span></div>
    <div class="days"><span></span><span></span><span></span><span></span><span></span><span></span><span>1</span><span>2</span><span>3</span><span>4</span><span>5</span><span>6</span><span>7</span><span>8</span><span>9</span><span>10</span><span>11</span><span>12</span><span>13</span><span>14</span><span>15</span><span>16</span><span>17</span><span>18</span><span>19</span><span>20</span><span>21</span><span>22</span><span>23</span><span>24</span><span>25</span><span>26</span><span>27</span><span>28</span><span>29</span><span>30</span><span>31</span></div>
  </section>
  <section class="month season-growing" style="left:387px;top:682px">
    <div class="month-head"><span class="month-tag">SEPTEMBER</span><span class="month-year">2020</span></div>
    <div class="weekdays"><span>SUN</span><span>MON</span><span>TUE</span><span>WED</span><span>THU</span><span>FRI</span><span>SAT</span></div>
    <div class="days"><span></span><span></span><span>1</span><span>2</span><span>3</span><span>4</span><span>5</span><span>6</span><span>7</span><span>8</span><span>9</span><span>10</span><span>11</span><span>12</span><span>13</span><span>14</span><span>15</span><span>16</span><span>17</span><span>18</span><span>19</span><span>20</span><span>21</span><span>22</span><span>23</span><span>24</span><span>25</span><span>26</span><span>27</span><span>28</span><span>29</span><span>30</span></div>
  </section>

  <!-- Season key -->
  <div class="key season-harvest" style="top:331px;height:96px"><span class="key-label">HARVESTING</span></div>
  <div class="key season-liming" style="top:448px;height:96px"><span class="key-label small">LIMING+FERTILISING</span></div>
  <div class="key season-sowing" style="top:567px;height:96px"><span class="key-label">SOWING</span></div>
  <div class="key season-growing" style="top:686px;height:96px"><span class="key-label">GROWING</span></div>

  <footer class="footer">
    <div class="brand">
      <div class="brand-name"><span class="brand-mark"></span><span>BREVARD HOLDINGS</span></div>
      <div class="brand-tag">GRAIN, FERTILISER, TRANSPORT, STORAGE</div>
    </div>
    <ul class="services">
      <li>- Buy and sell grain + stock feed at great prices</li>
      <li>- Buy fertiliser / lime / gypsum</li>
      <li>- Store or sell your grain at harvest</li>
      <li>- Move your bulk goods across NSW , VIC, QLD &amp; SA</li>
    </ul>
    <div class="contact">
      <div class="contact-icons">
        <svg viewBox="0 0 10 10"><path d="M2 0.5 L4 2.5 L3 4 Q4.5 6 6 7 L7.5 6 L9.5 8 L8 9.5 Q3 9 0.5 2 Z" fill="var(--growing)"/></svg>
        <svg viewBox="0 0 10 10"><rect x="0.5" y="2" width="9" height="6.5" fill="var(--growing)"/><path d="M0.5 2 L5 6 L9.5 2" stroke="#fff" fill="none"/></svg>
        <svg viewBox="0 0 10 10"><circle cx="5" cy="5" r="4.2" fill="none" stroke="var(--growing)"/><path d="M0.8 5 H9.2 M5 0.8 Q2 5 5 9.2 M5 0.8 Q8 5 5 9.2" stroke="var(--growing)" fill="none" stroke-width=".8"/></svg>
      </div>
      <div>02 6100 4827</div>
      <div>admin@brevardholdings.com.au</div>
      <div>www.brevardholdings.com.au</div>
    </div>
    <div class="address">
      <svg class="address-icon" viewBox="0 0 10 10"><path d="M5 0.5 L9.5 5 H8 V9.5 H2 V5 H0.5 Z" fill="var(--growing)"/></svg>
      <div>14 Mill Road</div>
      <div>Tarrin NSW 2700</div>
      <div>Australia</div>
    </div>
    <svg class="base" viewBox="0 0 600 18" preserveAspectRatio="none" aria-hidden="true">
      <polygon points="0,18 0,15 600,0 600,18" fill="var(--brand-green)"/>
      <polygon points="0,18 0,11 240,18" fill="var(--brand-blue)"/>
    </svg>
  </footer>
</main>
</body>
</html>
```